Life Coach for Lawyers Business Card Design

Elegant, original, business card design for life coaching service for associate attorneys who work in big law and struggle with stress, overwhelm, and time management. Double sided design.

Target Market(s)

Women associate attorneys who work in big law and struggle with stress, overwhelm, and time management.

Industry/Entity Type

Life Coaching

Contact Information for Business Card

Marissa Pendrell
Life Coach
518.677.3941
calmbriefcounsel.net
marissa@calmbriefcounsel.net
@calmbriefcounsel (Instagram)

Font styles to use
Other font styles liked:
• Silver South font duo. See uploaded files.

Requirements
Must have
• Icons for phone, website, email, and Instagram instead of words. Specific colors used in my logo (171B2B, 421121, FFFFFF)
Nice to have
• Foil. Embossed. Feminine design.
Should not have
• Any colors other than those used in logo. See uploaded files.

```html
<!DOCTYPE html>
<html lang="en">
<head>
<meta charset="utf-8">
<title>Calm Brief Counsel – Business Card</title>
<link rel="stylesheet" href="https://fonts.googleapis.com/css2?family=Jost:wght@300;400&family=Playfair+Display:wght@400&display=swap">
<style>
  :root {
    --plum: #421121;
    --navy: #171B2B;
    --white: #FFFFFF;
    --backdrop: #E8E6E3;
    --muted: #B9A3AC;
  }
  * { margin: 0; padding: 0; box-sizing: border-box; }
  html, body { width: 1200px; height: 1200px; overflow: hidden; }
  body {
    background: var(--backdrop);
    display: flex;
    flex-direction: column;
    align-items: center;
    justify-content: center;
    gap: 60px;
    font-family: "Jost", sans-serif;
  }
  .card {
    position: relative;
    width: 760px;
    height: 434px;
    background: var(--white);
    box-shadow: 0 10px 30px rgba(23, 27, 43, 0.18);
    overflow: hidden;
  }
  /* Front */
  .card-front { display: flex; align-items: center; justify-content: center; }
  .brand-name {
    font-family: "Playfair Display", serif;
    font-weight: 400;
    font-size: 56px;
    letter-spacing: 1px;
    color: var(--plum);
  }
  /* Back */
  .back-shapes { position: absolute; inset: 0; }
  .identity {
    position: absolute;
    left: 56px;
    top: 62px;
    color: var(--white);
  }
  .identity-name {
    font-weight: 300;
    font-size: 38px;
    letter-spacing: 1px;
  }
  .identity-title {
    margin-top: 6px;
    font-weight: 300;
    font-size: 21px;
    letter-spacing: 1px;
    color: var(--muted);
  }
  .contact-list {
    position: absolute;
    left: 56px;
    top: 256px;
    list-style: none;
    color: var(--plum);
    font-size: 15px;
    font-weight: 400;
  }
  .contact-item {
    display: flex;
    align-items: center;
    gap: 14px;
    margin-bottom: 14px;
    line-height: 1.2;
  }
  .contact-icon { width: 20px; height: 20px; flex: none; }
</style>
</head>
<body>

  <section class="card card-front" aria-label="Card front">
    <div class="brand-name">Calm Brief Counsel</div>
  </section>

  <section class="card card-back" aria-label="Card back">
    <svg class="back-shapes" viewBox="0 0 760 434" width="760" height="434" aria-hidden="true">
      <polygon points="0,0 432,0 416,200 0,212" fill="var(--plum)"/>
      <polygon points="452,0 760,0 760,318 438,212" fill="var(--plum)"/>
    </svg>

    <div class="identity">
      <div class="identity-name">Marissa Pendrell</div>
      <div class="identity-title">Life Coach</div>
    </div>

    <ul class="contact-list">
      <li class="contact-item">
        <svg class="contact-icon" viewBox="0 0 24 24" fill="none" stroke="var(--plum)" stroke-width="1.6" aria-hidden="true">
          <path d="M5 3h4l2 5-2.5 1.5a11 11 0 0 0 6 6L16 13l5 2v4a2 2 0 0 1-2 2A16 16 0 0 1 3 5a2 2 0 0 1 2-2z"/>
        </svg>
        <span>518.677.3941</span>
      </li>
      <li class="contact-item">
        <svg class="contact-icon" viewBox="0 0 24 24" fill="none" stroke="var(--plum)" stroke-width="1.6" aria-hidden="true">
          <rect x="3" y="5" width="18" height="14" rx="1"/>
          <path d="M3 6l9 7 9-7"/>
        </svg>
        <span>marissa@calmbriefcounsel.net</span>
      </li>
      <li class="contact-item">
        <svg class="contact-icon" viewBox="0 0 24 24" fill="none" stroke="var(--plum)" stroke-width="1.6" aria-hidden="true">
          <circle cx="12" cy="12" r="9"/>
          <path d="M3 12h18M12 3c3 3 3 15 0 18M12 3c-3 3-3 15 0 18"/>
        </svg>
        <span>www.calmbriefcounsel.net</span>
      </li>
      <li class="contact-item">
        <svg class="contact-icon" viewBox="0 0 24 24" fill="none" stroke="var(--plum)" stroke-width="1.6" aria-hidden="true">
          <circle cx="12" cy="12" r="8"/>
        </svg>
        <span>@calmbriefcounsel</span>
      </li>
    </ul>
  </section>

</body>
</html>
```